Business Card Design for Event Planning Company

Create a business card for event planning company using our new logo. After I pick the design, I will need files made for 6 employees. Our company provides event design & logistics services as well as venue management. The font should be sans serif and complementary to the logo. I will need to know the name of the font selected for the final design. The phone numbers listed should be separated by "." not "-"

Address for the card
PO Box 218, Washington, DC 20019

Card One
Lorna Pettigrew
lpettigrew@galaplanora.com
202.481.7032

Card Two
Marisol Dunleavy
mdunleavy@galaplanora.com
202.416.2950

Card Three
Rebecca Vasquetti
rvasquetti@galaplanora.com
978.527.6043

Card Four
Tessa Brink
tbrink@galaplanora.com
202.458.1276

Card Five
Ada-Rose Pemberton-Nwaku
adarose@galaplanora.com
202.819.3047

Card Six
Valerie Thornbury
Valerie@galaplanora.com
202.592.8134

Target Market(s)

Corporate/Non-Profit

Industry/Entity Type

Event Planning

Contact Information for Business Card

Address for the card

Card One
Lorna Pettigrew
lpettigrew@galaplanora.com
202.481.7032

Card Two
Marisol Dunleavy
202.416.2950

Card Three
Rebecca Vasquetti
978.527.6043

Card Four
Tessa Brink
tbrink@galaplanora.com
202.458.1276

Card Five
Ada-Rose Pemberton-Nwaku
202.819.3047

Card Six
Valerie Thornbury
202.592.8134

Font styles to use
Sans Serif

Colors

Designer to choose colors to be used in the design.

Requirements
Must have
• Two-sided with logo
Should not have
• Extra colors or be too busy

```html
<!DOCTYPE html>
<html lang="en">
<head>
<meta charset="utf-8">
<title>Gala Planora — Business Card</title>
<link rel="stylesheet" href="https://fonts.googleapis.com/css2?family=Montserrat:wght@300;400;700&display=swap">
<style>
  :root {
    --stage: #0b0b0b;
    --paper: #f9f7f2;
    --teal: #66aaa7;
    --ink: #151515;
    --text: #2a2a2a;
  }
  * { box-sizing: border-box; margin: 0; padding: 0; }
  html, body {
    width: 1200px; height: 1000px; overflow: hidden;
    background: var(--stage);
    font-family: "Montserrat", Arial, sans-serif;
  }
  .canvas { position: relative; width: 1200px; height: 1000px; }
  .card {
    position: absolute;
    width: 500px; height: 286px;
    background: var(--paper);
    border-radius: 18px;
    overflow: hidden;
  }
  .card--contact { left: 80px; top: 250px; }
  .card--brand { left: 620px; top: 460px; }

  /* contact side */
  .contact { position: absolute; left: 40px; top: 84px; color: var(--text); }
  .contact__name { font-weight: 700; font-size: 21px; color: var(--ink); margin-bottom: 10px; }
  .contact__name .surname { color: var(--teal); }
  .contact__address { font-size: 12.5px; line-height: 1.45; margin-bottom: 6px; }
  .contact__line { display: flex; align-items: center; gap: 7px; font-size: 12.5px; line-height: 1.6; }
  .contact__line svg { width: 12px; height: 12px; fill: var(--teal); flex: none; }

  .mark { display: flex; align-items: center; gap: 8px; }
  .mark__dot { width: 16px; height: 16px; border-radius: 50%; background: var(--teal); flex: none; }
  .mark__name { font-weight: 300; color: var(--ink); white-space: nowrap; }
  .mark--small { position: absolute; right: 34px; top: 92px; }
  .mark--small .mark__name { font-size: 22px; }

  /* brand side */
  .brand__band { position: absolute; top: 0; bottom: 0; }
  .brand__band--teal { left: 0; width: 56px; background: var(--teal); }
  .brand__band--ink { right: 0; width: 28px; background: var(--ink); }
  .brand__center {
    position: absolute; top: 0; bottom: 0; left: 56px; right: 28px;
    display: flex; align-items: center; justify-content: center;
  }
  .mark--large .mark__name { font-size: 42px; }
  .mark--large .mark__dot { width: 20px; height: 20px; }
</style>
</head>
<body>
<main class="canvas">
  <section class="card card--contact">
    <div class="contact">
      <p class="contact__name">Lorna <span class="surname">Pettigrew</span></p>
      <p class="contact__address">PO Box 218<br>Washington, DC 20019</p>
      <p class="contact__line">
        <svg viewBox="0 0 24 24" aria-hidden="true"><path d="M6.6 10.8a15.1 15.1 0 0 0 6.6 6.6l2.2-2.2c.3-.3.7-.4 1-.2 1.1.4 2.3.6 3.6.6.6 0 1 .4 1 1V20c0 .6-.4 1-1 1A17 17 0 0 1 3 4c0-.6.4-1 1-1h3.5c.6 0 1 .4 1 1 0 1.3.2 2.5.6 3.6.1.3 0 .7-.2 1z"/></svg>
        202.481.7032
      </p>
      <p class="contact__line">
        <svg viewBox="0 0 24 24" aria-hidden="true"><path d="M2 5h20v14H2zM4 7v.5l8 5 8-5V7z"/></svg>
        lpettigrew@galaplanora.com
      </p>
    </div>
    <div class="mark mark--small">
      <span class="mark__dot"></span>
      <span class="mark__name">galaplanora</span>
    </div>
  </section>

  <section class="card card--brand">
    <div class="brand__band brand__band--teal"></div>
    <div class="brand__band brand__band--ink"></div>
    <div class="brand__center">
      <div class="mark mark--large">
        <span class="mark__dot"></span>
        <span class="mark__name">galaplanora</span>
      </div>
    </div>
  </section>
</main>
</body>
</html>
```